Coral Sleep Depot Website

Need a design for a local Coral Sleep Depot Store.
The store is called Coral Sleep Depot.
need it to be something that customers can find on the internet and will
give them my location, they need to know i have the same brand mattress as the other store except i have them at almost half the price.

the office phone number is (786)555-0143
the office address is: 4127 sw Heron Bend Ave, Miami FL 33190

included is the logo, id like to stick the with white and teal design

here are is an excerpt that can or cannot be included

"We are a premium mattress discount outlet store located in South Florida; offering Free Delivery to Broward Miami-Dade, the Keys, and Palm Beach.

We carry the best brands in the market: Varnell CloudHaven; Dorvik SpineAlign, Brackett & Lowe, Pendry, among others.

We are open 7 days a week, and we are accessible from all major highways. We are a family business and our goal is to provide you with the most comfortable and best quality mattress at a price that has no competition. Come visit us and take a look at our large inventory selection."

```html
<!DOCTYPE html>
<html lang="en">
<head>
<meta charset="utf-8">
<title>Coral Sleep Depot</title>
<link rel="stylesheet" href="https://fonts.googleapis.com/css2?family=Source+Sans+3:ital,wght@0,400;0,600;1,400&display=swap">
<style>
  :root {
    --teal: #13a8c8;
    --teal-dark: #0f93b0;
    --ink: #333333;
    --muted: #6b6b6b;
    --page: #ffffff;
    --band: #f4f4f4;
    --footer: #4b4b4d;
    --footer-text: #e4e4e4;
    --footer-muted: #bdbdbd;
    --rule: #6a6a6c;
  }
  * { box-sizing: border-box; margin: 0; padding: 0; }
  html, body { width: 1200px; height: 1129px; overflow: hidden; }
  body {
    position: relative;
    background: var(--page);
    font-family: "Source Sans 3", Arial, sans-serif;
    color: var(--ink);
  }
  h1, h2, h3 { font-weight: 400; }
  .abs { position: absolute; }

  /* header */
  .brand-dot { left: 326px; top: 50px; width: 12px; height: 12px; background: var(--teal); border-radius: 50%; }
  .brand {
    left: 346px; top: 40px; white-space: nowrap;
    font-size: 24px; line-height: 30px; font-weight: 600;
    color: var(--ink); letter-spacing: 0.2px;
  }
  .contact-bar { left: 672px; top: 18px; width: 240px; display: flex; align-items: center; justify-content: flex-end; gap: 6px; font-size: 8.5px; color: var(--ink); white-space: nowrap; }
  .contact-bar svg { flex: none; }
  .contact-bar .gap { width: 6px; }
  .nav { top: 57px; left: 686px; width: 226px; display: flex; justify-content: space-between; font-size: 10px; color: var(--ink); white-space: nowrap; }
  .nav .active { color: var(--teal); text-decoration: underline; text-underline-offset: 2px; }

  /* hero */
  .hero-photo {
    left: 326px; top: 156px; width: 345px; height: 230px;
    background: linear-gradient(160deg, #f7f4ee 0%, #ebe5d8 55%, #d9d1c0 100%);
    border-radius: 4px;
  }
  .hero-title { left: 688px; top: 124px; font-size: 27px; line-height: 32px; color: var(--teal); letter-spacing: 0.3px; white-space: nowrap; }
  .hero-sub { left: 691px; top: 158px; font-size: 10.5px; color: var(--ink); white-space: nowrap; }
  .hero-rule { left: 692px; top: 189px; width: 204px; height: 1px; background: #d6d6d6; }
  .hero-copy { left: 692px; top: 199px; width: 205px; font-size: 8px; line-height: 10.5px; color: var(--muted); }
  .btn {
    left: 816px; top: 263px; width: 79px; height: 27px;
    background: var(--teal); color: #fff; font-size: 9.5px; font-weight: 600;
    display: flex; align-items: center; justify-content: center; border-radius: 2px;
  }

  /* features band */
  .band { left: 0; top: 440px; width: 1200px; height: 415px; background: var(--band); }
  .band-shadow { left: 0; top: 440px; width: 1200px; height: 20px; background: linear-gradient(#dcdcdc, rgba(244,244,244,0)); }
  .section-title { font-size: 14px; color: var(--ink); white-space: nowrap; }
  .feature-title { font-size: 9.5px; color: var(--teal); white-space: nowrap; }
  .feature-copy { width: 360px; font-size: 8px; line-height: 10.5px; color: var(--muted); }
  .feature-icon { left: 327px; }
  .hours-copy { left: 750px; top: 530px; width: 165px; font-size: 8px; line-height: 10.5px; color: var(--muted); }
  .hours-line { left: 750px; font-size: 8.5px; color: var(--ink); white-space: nowrap; }
  .hours-line .accent { color: var(--teal); }

  .thumb { top: 700px; width: 135px; height: 96px; }
  .thumb-1 { left: 326px; background: linear-gradient(135deg, #efe8d6, #cfc3a5); }
  .thumb-2 { left: 476px; background: linear-gradient(135deg, #b98a58 0%, #eeeeee 40%, #d9d9d9 100%); }
  .thumb-3 { left: 629px; background: linear-gradient(135deg, #7d7d7d, #5c5c5c); }
  .thumb-4 { left: 778px; background: linear-gradient(135deg, #ffffff, #e7e3df); }
  .thumb-caption { left: 629px; top: 743px; width: 135px; text-align: center; font-size: 8px; font-weight: 600; color: #fff; }
  .thumb-plus { width: 11px; height: 11px; border-radius: 50%; background: var(--teal); color: #fff; font-size: 10px; line-height: 11px; text-align: center; top: 778px; }
  .thumb-plus.ghost { background: transparent; border: 1px solid #fff; line-height: 9px; }

  /* footer */
  .footer { left: 0; top: 855px; width: 1200px; height: 274px; background: var(--footer); }
  .footer-brand { left: 327px; top: 924px; white-space: nowrap; font-size: 21px; line-height: 24px; font-weight: 600; color: #ffffff; }
  .footer-about { left: 326px; top: 986px; width: 200px; font-size: 7.5px; line-height: 10.3px; font-style: italic; color: var(--footer-text); }
  .footer-title { top: 908px; font-size: 14px; color: #ffffff; white-space: nowrap; }
  .footer-text { font-size: 7.5px; line-height: 10.5px; color: var(--footer-text); }
  .footer-addr { font-size: 9px; line-height: 15px; color: var(--footer-text); white-space: nowrap; }
  .social { top: 981px; width: 16px; height: 16px; border-radius: 50%; background: #c9c9c9; }
  .social.active { background: var(--teal); }
  .footer-rule { left: 326px; top: 1085px; width: 586px; height: 1px; background: var(--rule); }
  .legal { left: 327px; top: 1105px; font-family: Arial, sans-serif; font-size: 7.5px; color: var(--footer-muted); white-space: nowrap; }
  .legal .accent { color: var(--teal); }
</style>
</head>
<body>

  <!-- header -->
  <div class="abs brand-dot"></div>
  <div class="abs brand">Coral Sleep Depot</div>

  <div class="abs contact-bar">
    <svg width="11" height="11" viewBox="0 0 12 12"><circle cx="6" cy="6" r="6" fill="#13a8c8"/><path d="M4 3.2c.4-.3.8-.2 1 .2l.5 1c.1.3 0 .6-.2.8l-.3.3c.3.7.8 1.2 1.5 1.5l.3-.3c.2-.2.5-.3.8-.2l1 .5c.4.2.5.6.2 1-.5.7-1.3.9-2.1.5C5.3 7.8 4.2 6.7 3.5 5.3c-.4-.8-.2-1.6.5-2.1z" fill="#fff"/></svg>
    <span>(786)555-0143</span>
    <span class="gap"></span>
    <svg width="11" height="11" viewBox="0 0 12 12"><circle cx="6" cy="6" r="6" fill="#13a8c8"/><path d="M6 2.6a2.3 2.3 0 0 0-2.3 2.3C3.7 6.6 6 9.4 6 9.4s2.3-2.8 2.3-4.5A2.3 2.3 0 0 0 6 2.6zm0 3.2a.9.9 0 1 1 0-1.8.9.9 0 0 1 0 1.8z" fill="#fff"/></svg>
    <span>4127 sw Heron Bend Ave, Miami FL 33190</span>
  </div>

  <nav class="abs nav">
    <span class="active">Home</span>
    <span>Brand Mattress</span>
    <span>Our Location</span>
    <span>Contact Us</span>
  </nav>

  <!-- hero -->
  <div class="abs hero-photo" role="img" aria-label="White mattress on a box base with pillows and a folded gold throw"></div>
  <h1 class="abs hero-title">WAKE REFRESHED</h1>
  <p class="abs hero-sub">Advance Mattress Technology For Active Life Style</p>
  <div class="abs hero-rule"></div>
  <p class="abs hero-copy">Lorem Ipsum is simply dummy text of the printing and typesetting industry. Lorem Ipsum has been the industry's standard dummy text ever since</p>
  <a class="abs btn">LEARN MORE</a>

  <!-- features band -->
  <div class="abs band"></div>
  <div class="abs band-shadow"></div>

  <h2 class="abs section-title" style="left:327px; top:502px;">Mattress Features</h2>

  <svg class="abs feature-icon" style="top:536px;" width="11" height="8" viewBox="0 0 11 8"><path d="M1 4h8M6 1l3 3-3 3" stroke="#13a8c8" stroke-width="1.6" fill="none" stroke-linecap="round" stroke-linejoin="round"/></svg>
  <h3 class="abs feature-title" style="left:351px; top:534px;">A complete Mattress Showroom</h3>
  <p class="abs feature-copy" style="left:351px; top:548px;">Lorem Ipsum is simply dummy text of the printing and typesetting industry. Lorem Ipsum has been the industry's standard dummy text ever since</p>

  <svg class="abs feature-icon" style="top:589px;" width="11" height="8" viewBox="0 0 11 8"><path d="M1 4h8M6 1l3 3-3 3" stroke="#13a8c8" stroke-width="1.6" fill="none" stroke-linecap="round" stroke-linejoin="round"/></svg>
  <h3 class="abs feature-title" style="left:351px; top:587px;">A complete Mattress Showroom</h3>
  <p class="abs feature-copy" style="left:351px; top:601px;">Lorem Ipsum is simply dummy text of the printing and typesetting industry. Lorem Ipsum has been the industry's standard dummy text ever since</p>

  <h2 class="abs section-title" style="left:749px; top:502px;">Store Hour</h2>
  <p class="abs hours-copy">Lorem Ipsum is simply dummy text of the printing and typesetting industry. Lorem Ipsum has been the industry's standard dummy text ever since</p>
  <p class="abs hours-line" style="top:586px;">MON-SAT 09a.m - 07 p.m</p>
  <p class="abs hours-line" style="top:600px;"><span class="accent">After Hours</span>: By Appointment Only</p>

  <h2 class="abs section-title" style="left:327px; top:668px;">Coral Sleep Depot Store</h2>

  <div class="abs thumb thumb-1" role="img" aria-label="Close view of a quilted cream mattress top"></div>
  <div class="abs thumb thumb-2" role="img" aria-label="Made bed with white linens beside a wooden wall"></div>
  <div class="abs thumb thumb-3" role="img" aria-label="Tufted mattress corner under a dark hover overlay"></div>
  <div class="abs thumb thumb-4" role="img" aria-label="Person sleeping on white pillows"></div>
  <p class="abs thumb-caption">Lorem Ipsum is simply dummy</p>
  <div class="abs thumb-plus" style="left:440px;">+</div>
  <div class="abs thumb-plus" style="left:592px;">+</div>
  <div class="abs thumb-plus ghost" style="left:745px;">+</div>
  <div class="abs thumb-plus" style="left:897px;">+</div>

  <!-- footer -->
  <footer class="abs footer"></footer>
  <div class="abs footer-brand">Coral Sleep Depot</div>
  <p class="abs footer-about">Lorem Ipsum is simply dummy text of the printing and typesetting industry. Lorem Ipsum has been the industry's standard dummy text ever since the 1500s, when an unknown printer took a galley of type and scrambled it to make a type specimen book. It has survived not only five centuries, but also the leap into electronic typesetting, remaining essentially unchanged.</p>

  <h2 class="abs footer-title" style="left:573px;">Office Location</h2>
  <p class="abs footer-text" style="left:575px; top:942px; width:160px;">Feel free to contact us and find out how we can help you find your perfect mattress.</p>
  <p class="abs footer-addr" style="left:575px; top:983px;">4127 sw Heron Bend Ave<br>Miami FL 33190</p>
  <p class="abs footer-addr" style="left:575px; top:1026px;">Call:&nbsp; (786)555-0143</p>

  <h2 class="abs footer-title" style="left:771px;">Get Social With Us</h2>
  <p class="abs footer-text" style="left:773px; top:942px; width:140px;">Lorem Ipsum is simply dummy text of the printing and typesetting industry</p>
  <div class="abs social active" style="left:774px;"></div>
  <div class="abs social" style="left:796px;"></div>
  <div class="abs social" style="left:818px;"></div>

  <div class="abs footer-rule"></div>
  <p class="abs legal">Copyright © 2014 Company Name.&nbsp; All Rights Reserved.&nbsp; |&nbsp; <span class="accent">Privacy Policy</span>&nbsp; |&nbsp; Terms &amp; Condition</p>

</body>
</html>
```